RIVERSTONE PAVING & EARTHWORKS

I would like the front of the card to have my logo centred.
I need it to have my contact details on the back of the card which are: RiverstonePavingEarthworks@mailbrook.net
0439268417
and a Friendbook icon

```html
<!DOCTYPE html>
<html lang="en">
<head>
<meta charset="utf-8">
<title>Riverstone Paving &amp; Earthworks – Business Card</title>
<link href="https://fonts.googleapis.com/css2?family=Poppins:wght@400;500;600;700&family=Roboto:wght@400;700&display=swap" rel="stylesheet">
<style>
  :root {
    --brand-blue: #1374b3;
    --sky-blue: #22b8e6;
    --deep-blue: #0b4a91;
    --ink: #111111;
    --black: #000000;
    --white: #ffffff;
    --grey-light: #bdbdbd;
    --grey-dark: #7a7a7a;
    --frame: #5a5a5a;
  }
  html, body {
    margin: 0;
    padding: 0;
    width: 1200px;
    height: 848px;
    overflow: hidden;
    background: var(--white);
  }
  .sheet {
    position: relative;
    width: 1200px;
    height: 848px;
  }
  .card {
    position: absolute;
    width: 520px;
    height: 297px;
    box-sizing: border-box;
    overflow: hidden;
  }
  .card--contact {
    left: 69px;
    top: 120px;
    background: var(--white);
    border: 1.5px solid var(--frame);
  }
  .card--brand {
    left: 614px;
    top: 435px;
    background: var(--black);
  }
  .card__shapes {
    position: absolute;
    inset: 0;
  }
  .person {
    position: absolute;
    left: 13px;
    top: 66px;
    z-index: 2;
  }
  .person__name {
    margin: 0;
    font-family: "Roboto", sans-serif;
    font-weight: 700;
    font-size: 25px;
    line-height: 1;
    color: var(--brand-blue);
  }
  .person__role {
    margin: 3px 0 0;
    font-family: "Roboto", sans-serif;
    font-weight: 400;
    font-size: 16px;
    color: var(--ink);
  }
  .contact-list {
    position: absolute;
    left: 13px;
    top: 123px;
    margin: 0;
    padding: 0;
    list-style: none;
    z-index: 2;
  }
  .contact-list__item {
    display: flex;
    align-items: center;
    height: 21px;
    margin-bottom: 8.5px;
    font-family: "Poppins", sans-serif;
    font-weight: 500;
    font-size: 12px;
    color: var(--ink);
  }
  .contact-list__item--email { font-size: 11px; }
  .contact-list__item--phone { font-size: 13.5px; font-weight: 400; }
  .contact-list__icon {
    width: 21px;
    height: 21px;
    margin-right: 7px;
    flex: none;
  }
  .social {
    position: absolute;
    left: 12px;
    top: 250px;
    display: flex;
    align-items: center;
    gap: 10px;
    z-index: 2;
  }
  .social__item {
    display: flex;
    align-items: center;
    gap: 5px;
    font-family: "Poppins", sans-serif;
    font-weight: 500;
    font-size: 10.5px;
    color: var(--brand-blue);
  }
  .social__badge {
    width: 28px;
    height: 28px;
    border-radius: 50%;
    background: var(--brand-blue);
    flex: none;
  }
  .brand-mark {
    position: absolute;
    display: flex;
    flex-direction: column;
    align-items: center;
    text-align: center;
    font-family: "Poppins", sans-serif;
    font-weight: 700;
    color: var(--sky-blue);
    z-index: 2;
  }
  .brand-mark__square {
    background: var(--brand-blue);
  }
  .brand-mark--small {
    left: 300px;
    top: 24px;
    width: 205px;
    font-size: 15px;
    line-height: 1.2;
  }
  .brand-mark--small .brand-mark__square {
    width: 44px;
    height: 44px;
    margin-bottom: 10px;
  }
  .brand-mark--large {
    left: 0;
    top: 52px;
    width: 520px;
    font-size: 30px;
    line-height: 1.2;
  }
  .brand-mark--large .brand-mark__square {
    width: 96px;
    height: 96px;
    margin-bottom: 18px;
  }
</style>
</head>
<body>
<main class="sheet">

  <section class="card card--contact" aria-label="Card back with contact details">
    <svg class="card__shapes" width="520" height="297" viewBox="0 0 520 297" aria-hidden="true">
      <defs>
        <linearGradient id="greyFade" x1="0" y1="0" x2="0" y2="1">
          <stop offset="0" stop-color="#bdbdbd"/>
          <stop offset="1" stop-color="#7a7a7a"/>
        </linearGradient>
        <linearGradient id="blueFade" x1="0" y1="0" x2="0" y2="1">
          <stop offset="0" stop-color="#22b8e6"/>
          <stop offset="1" stop-color="#0b4a91"/>
        </linearGradient>
      </defs>
      <polygon class="hex hex--grey-large" points="318,39 385,77 385,156 318,195 251,156 251,77" fill="url(#greyFade)"/>
      <polygon class="shield" points="300,0 505,0 505,156 404,215 300,156" fill="#000000"/>
      <polygon class="hex hex--grey-small" points="361,202 389,218 389,251 361,267 332,251 332,218" fill="url(#greyFade)"/>
      <polygon class="hex hex--blue" points="462,161 513,190 513,248 462,277 412,248 412,190" fill="url(#blueFade)"/>
    </svg>

    <div class="brand-mark brand-mark--small">
      <span class="brand-mark__square"></span>
      <span>RIVERSTONE PAVING<br>&amp; EARTHWORKS</span>
    </div>

    <header class="person">
      <h1 class="person__name">DANIEL HARLOW</h1>
      <p class="person__role">Creative Director</p>
    </header>

    <ul class="contact-list">
      <li class="contact-list__item">
        <svg class="contact-list__icon" viewBox="0 0 21 21" aria-hidden="true">
          <circle cx="10.5" cy="10.5" r="10.5" fill="#1374b3"/>
          <path d="M10.5 5a3.3 3.3 0 0 0-3.3 3.3c0 2.5 3.3 6.7 3.3 6.7s3.3-4.2 3.3-6.7A3.3 3.3 0 0 0 10.5 5z" fill="#ffffff"/>
          <circle cx="10.5" cy="8.3" r="1.2" fill="#1374b3"/>
        </svg>
        Street Name, City, State
      </li>
      <li class="contact-list__item">
        <svg class="contact-list__icon" viewBox="0 0 21 21" aria-hidden="true">
          <circle cx="10.5" cy="10.5" r="10.5" fill="#1374b3"/>
          <rect x="5.5" y="6.5" width="6" height="4" rx="2" transform="rotate(40 8.5 8.5)" fill="none" stroke="#ffffff" stroke-width="1.3"/>
          <rect x="9.5" y="10.5" width="6" height="4" rx="2" transform="rotate(40 12.5 12.5)" fill="none" stroke="#ffffff" stroke-width="1.3"/>
        </svg>
        www.riverstonepaving.net
      </li>
      <li class="contact-list__item contact-list__item--email">
        <svg class="contact-list__icon" viewBox="0 0 21 21" aria-hidden="true">
          <circle cx="10.5" cy="10.5" r="10.5" fill="#1374b3"/>
          <rect x="5.5" y="7" width="10" height="7" fill="none" stroke="#ffffff" stroke-width="1.2"/>
          <path d="M5.5 7l5 4 5-4M5.5 14l3.5-3.3M15.5 14L12 10.7" fill="none" stroke="#ffffff" stroke-width="1.1"/>
        </svg>
        RiverstonePavingEarthworks@mailbrook.net
      </li>
      <li class="contact-list__item contact-list__item--phone">
        <svg class="contact-list__icon" viewBox="0 0 21 21" aria-hidden="true">
          <circle cx="10.5" cy="10.5" r="10.5" fill="#1374b3"/>
          <path d="M7.2 5.5c.5-.4 1.1-.3 1.4.2l1 1.6c.3.5.2 1-.2 1.3l-.7.5c.5 1.2 1.4 2.2 2.6 2.8l.5-.7c.3-.4.9-.5 1.3-.2l1.6 1c.5.3.6.9.2 1.4l-.7.8c-.5.6-1.4.8-2.1.4-2.6-1.3-4.5-3.3-5.6-5.9-.3-.8-.1-1.6.5-2.1z" fill="#ffffff"/>
        </svg>
        0439268417
      </li>
    </ul>

    <nav class="social" aria-label="Social channels">
      <span class="social__item"><span class="social__badge"></span>Friendbook</span>
      <span class="social__item"><span class="social__badge"></span>Snapgram</span>
      <span class="social__item"><span class="social__badge"></span>ChatWave</span>
    </nav>
  </section>

  <section class="card card--brand" aria-label="Card front with company name">
    <div class="brand-mark brand-mark--large">
      <span class="brand-mark__square"></span>
      <span>RIVERSTONE PAVING<br>&amp; EARTHWORKS</span>
    </div>
  </section>

</main>
</body>
</html>
```